Evermore Roofing flyer*

I need an a5 size flyer designing to go in our local advertising magazine.We are based in the north west of England Id like key features from the website including on the flyer, possibly even reviews, what we do ect.I don't however want it too busy, simple pictures and description of service.company colours and logo. I require simple one sided business cards toonumber, web address and logowinner will receive a request to design around 5 different double sided a5 flyers too, each with all our services on one side and the other primarily for one service we have provided locally with a spacve to put the house number down.REPAIRSROOFLINEFLAT ROOFS PITCHED ROOFSSYNTHETIC ROOFSUP TO 50 YEARS WARRANTY AVAILABLERANKED THE #1 FLAT ROOFER IN THE UK OUT OF 787 REGISTERED FLAT ROOFING COMPANIESRANKED THE #10 ROOFING COMPANY IN THE UK OUT OF 1976 REGISTERED SPECIALIST ROOFING COMPANIESBOTH FOR COST, CUSTOMER SERVICE AND QUALITY WITH 5 STAR REVIEWSGUARANTEED TO FIND AND FIX A LEAKAPPROVED INSTALLERSAWARD WINNINGTIME SERVED FIXED PRICES

Target Market(s)

homeowners

Colors

Designer to choose only greyscale colors for use in the design.

Requirements
Must have
• contact details
• pictures of my work
• clear and simple

```html
<!DOCTYPE html>
<html lang="en">
<head>
<meta charset="utf-8">
<title>Evermore Roofing – A5 Flyer</title>
<link href="https://fonts.googleapis.com/css2?family=Oswald:wght@500;600;700&family=PT+Sans:wght@400;700&family=Open+Sans:wght@800&family=Lilita+One&display=swap" rel="stylesheet">
<style>
  :root{
    --stage:#d4d4d4;
    --paper:#ffffff;
    --paper-top:#f3f3f3;
    --navy:#2b3040;
    --green:#2f7d2a;
    --green-dark:#236420;
    --green-light:#4a9a36;
    --yellow:#f4cf1f;
    --ink:#1a1a1a;
    --grey-bar:#9a9a9a;
    --band-grey:#dcdcdc;
  }
  *{box-sizing:border-box;margin:0;padding:0}
  html,body{width:1200px;height:1200px;overflow:hidden;background:var(--stage)}
  .flyer{
    position:absolute;left:206px;top:41px;width:788px;height:1118px;
    background:var(--paper);overflow:hidden;
    box-shadow:0 6px 18px rgba(0,0,0,.25);
  }
  .layer{position:absolute;left:0;top:0}
  .brand{
    position:absolute;left:30px;top:38px;
    font-family:"Oswald",sans-serif;font-weight:700;color:var(--green);
    font-size:46px;line-height:46px;letter-spacing:1px;text-transform:uppercase;
  }
  .hero-title{position:absolute;left:19px;top:190px;font-family:"Oswald",sans-serif;font-weight:600;text-transform:uppercase;line-height:1}
  .hero-title .lead{display:block;color:var(--yellow);font-size:50px}
  .hero-title .big{display:block;color:#fff;font-size:86px;letter-spacing:-1px;margin-top:2px}
  .hero-title .mid{display:block;color:#fff;font-size:66px;margin-top:8px}
  .cta{
    position:absolute;left:20px;top:446px;width:372px;height:55px;border-radius:14px;
    background:linear-gradient(#4c9d3a,#2c7a26);
    color:#fff;font-family:"PT Sans",sans-serif;font-weight:700;font-size:23px;
    display:flex;align-items:center;justify-content:center;
    box-shadow:0 3px 6px rgba(0,0,0,.35);
  }
  .section-head{
    position:absolute;top:556px;font-family:"Oswald",sans-serif;font-weight:600;
    color:var(--green);font-size:36px;line-height:40px;text-transform:uppercase;
    padding-left:16px;
  }
  .section-head::before{content:"";position:absolute;left:0;top:4px;width:6px;height:32px;background:var(--grey-bar)}
  .why{left:20px}
  .ranked{left:440px}
  .about{
    position:absolute;left:23px;top:609px;width:396px;
    font-family:"PT Sans",sans-serif;font-size:16.5px;line-height:21.3px;color:var(--ink);
    text-align:justify;
  }
  .work-photo{position:absolute;top:761px;width:195px;height:179px}
  .work-photo.tiles{left:20px;background:linear-gradient(135deg,#c9602a 0%,#b9a27a 45%,#8c8f96 100%)}
  .work-photo.house{left:224px;background:linear-gradient(160deg,#8fb4d6 0%,#7a3e2e 40%,#6b3325 70%,#b8764f 100%)}
  .services{position:absolute;left:438px;top:612px;width:326px;list-style:none}
  .service{position:relative;height:81px;display:flex;align-items:center;margin-bottom:0}
  .service.boxed{background:#fff;box-shadow:0 1px 6px rgba(0,0,0,.35)}
  .service .num{
    width:63px;text-align:center;font-family:"Oswald",sans-serif;font-weight:600;
    font-size:64px;line-height:1;color:var(--green);
    background:linear-gradient(#3f9a33,#1f5a1c);-webkit-background-clip:text;background-clip:text;-webkit-text-fill-color:transparent;
  }
  .service .label{font-family:"Open Sans",sans-serif;font-weight:800;font-size:24px;color:var(--ink);text-transform:uppercase;letter-spacing:.2px}
  .bubble{position:absolute;left:26px;top:1032px}
  .bubble-text{
    position:absolute;left:0;top:0;width:198px;height:54px;display:flex;align-items:center;justify-content:center;
    font-family:"Lilita One",sans-serif;font-size:26px;color:var(--yellow);letter-spacing:.5px;
    text-shadow:-1px -1px 0 #3a2a00,1px -1px 0 #3a2a00,-1px 1px 0 #3a2a00,1px 1px 0 #3a2a00;
  }
  .contact{
    position:absolute;left:240px;top:1035px;width:440px;text-align:center;
    font-family:"PT Sans",sans-serif;font-size:18px;line-height:23px;color:#fff;
  }
  .contact strong{font-weight:700}
</style>
</head>
<body>
<main class="flyer">

  <svg class="layer" width="788" height="1118" viewBox="0 0 788 1118" aria-hidden="true">
    <defs>
      <linearGradient id="navyFade" x1="0" x2="1" y1="0" y2="0">
        <stop offset="0" stop-color="#2b3040"/>
        <stop offset="0.42" stop-color="#2b3040" stop-opacity="0.95"/>
        <stop offset="0.62" stop-color="#2b3040" stop-opacity="0"/>
      </linearGradient>
      <linearGradient id="greenBand" x1="0" x2="0" y1="0" y2="1">
        <stop offset="0" stop-color="#3f8f30"/>
        <stop offset="1" stop-color="#2a6d25"/>
      </linearGradient>
    </defs>
    <rect x="0" y="0" width="788" height="529" fill="#f3f3f3"/>
    <polygon points="0,158 319,158 399,68 788,68 788,529 0,529" fill="url(#navyFade)"/>
    <polygon points="0,938 28,938 70,990 788,990 788,1118 0,1118" fill="#ffffff"/>
    <polygon points="30,985 788,985 788,1078 745,1078 685,1006 55,1006" fill="var(--band-grey)"/>
    <polygon points="0,938 55,1006 685,1006 745,1078 788,1078 788,1118 0,1118" fill="url(#greenBand)"/>
    <path d="M8 1000 h182 a18 18 0 0 1 18 18 v18 a18 18 0 0 1 -18 18 h-130 l-22 14 l6 -14 h-36 a18 18 0 0 1 -18 -18 v-18 a18 18 0 0 1 18 -18 z" transform="translate(18 32)" fill="#ffffff"/>
  </svg>

  <div class="layer" role="img" aria-label="Photo of two roofers laying underlay on a timber-framed pitched roof with a ladder against the eaves"
       style="left:0;top:68px;width:788px;height:461px;clip-path:polygon(319px 90px,399px 0,788px 0,788px 461px,0 461px,0 90px);background:linear-gradient(160deg,#8b8f62 0%,#b98a52 35%,#2e2f33 55%,#c99b62 80%,#a4784a 100%);z-index:0"></div>
  <svg class="layer" width="788" height="529" viewBox="0 0 788 529" aria-hidden="true" style="z-index:1">
    <polygon points="0,158 319,158 399,68 788,68 788,529 0,529" fill="url(#navyFade)"/>
  </svg>

  <div class="brand" style="z-index:2">Evermore<br>Roofing</div>

  <h1 class="hero-title" style="z-index:2">
    <span class="lead">Up to</span>
    <span class="big">50 Years</span>
    <span class="mid">Warranty</span>
  </h1>

  <a class="cta" style="z-index:2">Contact us for more information</a>

  <h2 class="section-head why">Why choose us</h2>
  <h2 class="section-head ranked">Ranked the #1</h2>

  <p class="about">Flat roofer in the uk out of 787 registered flat roofing companies ranked the #10. Roofing company in the uk out of 1976 registered specialist roofing companies both for cost, customer service and quality with 5 star reviews. Guaranteed to find and fix a leak approved installers award winning time served fixed prices.</p>

  <div class="work-photo tiles" role="img" aria-label="Photo of a roofer fitting terracotta tiles onto battens"></div>
  <div class="work-photo house" role="img" aria-label="Photo of a finished brown tiled roof with a skylight under blue sky"></div>

  <ol class="services">
    <li class="service boxed" style="height:83px"><span class="num">1</span><span class="label">Repairs Roofline</span></li>
    <li class="service"><span class="num">2</span><span class="label">Flat Roofs</span></li>
    <li class="service boxed" style="height:79px"><span class="num">3</span><span class="label">Pitched Roofs</span></li>
    <li class="service"><span class="num">4</span><span class="label">Synthetic Roofs</span></li>
  </ol>

  <div class="bubble"><span class="bubble-text">SAY HELLO!</span></div>

  <p class="contact">For More Information Contact us on <strong>0161 555 0142</strong> or<br>Email us at <strong>hello@evermoreroofing.co.uk</strong></p>

</main>
</body>
</html>
```